Endocrinologist needs new stationery

I have a logo from ArtHiveLab and now need stationery with the new logo.

Address: Suite 4, 238 Kestrel Lane, Richmond, VIC 3121
Phone: 03 9412 7053
Fax: 03 9412 7055
Website: www.drmelvaparkson.com.au
Email: admin@drmelvaparkson.com.au

```html
<!DOCTYPE html>
<html lang="en">
<head>
<meta charset="UTF-8">
<title>Dr Melva Parkson – Letterhead</title>
<link href="https://fonts.googleapis.com/css2?family=Montserrat:wght@400&display=swap" rel="stylesheet">
<style>
  :root {
    --paper: #ffffff;
    --brand-blue: #2a6fc9;
    --brand-purple: #5e3d7d;
    --ink-grey: #4a4c55;
  }
  * { margin: 0; padding: 0; box-sizing: border-box; }
  html, body {
    width: 856px;
    height: 1200px;
    overflow: hidden;
    background: var(--paper);
  }
  .letterhead {
    position: relative;
    width: 856px;
    height: 1200px;
    background: var(--paper);
    font-family: "Montserrat", sans-serif;
  }
  .brand-name {
    position: absolute;
    top: 78px;
    left: 0;
    width: 100%;
    text-align: center;
    font-size: 34px;
    font-weight: 400;
    letter-spacing: 1px;
    color: var(--brand-blue);
  }
  .footer-rule {
    position: absolute;
    top: 1072px;
    left: 105px;
    width: 653px;
    height: 1px;
    background: var(--brand-purple);
  }
  .contact {
    position: absolute;
    top: 1090px;
    left: 0;
    width: 100%;
    text-align: center;
    font-size: 15px;
    line-height: 19.5px;
    color: var(--ink-grey);
  }
  .contact .label { color: var(--brand-blue); }
  .contact .sep { display: inline-block; width: 6px; }
  .contact .web-domain { color: var(--brand-purple); }
</style>
</head>
<body>
  <main class="letterhead">
    <header>
      <div class="brand-name">Dr Melva Parkson</div>
    </header>

    <footer>
      <div class="footer-rule"></div>
      <address class="contact" style="font-style: normal;">
        <div class="contact-address">Suite 4, 238 Kestrel Lane, Richmond, VIC 3121</div>
        <div class="contact-lines">
          <span class="label">T :</span> 03 9412 7053<span class="sep"></span>
          <span class="label">F :</span> 03 9412 7055<span class="sep"></span>
          <span class="label">E :</span> admin@drmelvaparkson.com.au
        </div>
        <div class="contact-web">www.<span class="web-domain">drmelvaparkson</span>.com.au</div>
      </address>
    </footer>
  </main>
</body>
</html>
```